Flyer to Advertise Eyelash Extension Training Courses for Beauty Industry Professionals and Future

Hello,

I own an Eyelash and Skincare studio in Aliso Viejo, CA. www.velvetgloworks.com.We are now about to be offering a education side to our company where we offer courses to other beauty industry professionals or cosmetology students/future professionals. It will be called VGW ACADEMY. Our academies will have certain dates that will be on our website. I would like to make a flyer/menu of our new courses. You don't have to use all the information below but I've made it available for you. Please Re-word if necessary. Also you don't have to use the photos i've attached there just to help you see what I'm doing. Also I love the Look of Dora Whitfield brands, Lorvane, TEK, VILO, so I want this flyer to look really appealing to beauty industry professionals and future professionals.So be as creative as possible.

We have these courses:

1) Eyelash Enhancement Classic Extension Course
-1 Day Course. $350 and comes with a Kit that should last the students through 30 clients.
2) Eyelash Enhancement Russian Volume Course
-2 Day Course. $450 and comes with a kit that should last the students through 30 clients.
3)Threading Hair Removal Course
-1/2 Day course. $100 and comes with a kit that should last students through 60 clients. Students will need 3 Models for Eyebrow Threading
4)Spray Tanning Course
-1/2 Day course. $100 and will have an "add-on" kit that will get them a Spray tan Machine with 3 basic colors to last the student through 300 clients.

BUNDLE DEALS:
-Lash Pro Bundle: Students will learn Eyelash Enhancement Both Classic and Volume Extensions. 4 Day Course. $650 and comes with 2 kits for each technique.
-Velvet Pro Bundle: All of our courses combined. $850

MOBILE Options:
Call 949-387-6120 to inquire or email kelseyportland@velvetgloworks.com

Target Market(s)

Cosmetology Schools, Beauty Industry Students, Beauty industry professionals looking to seek add on services to provide to their clients.

Industry/Entity Type

Cosmetology

Font styles to use
Serif
Sans Serif
Decorative

Colors
f59296
f04a50
ffffff
000000
5c5c5c
aaaaaa

Requirements
Must have
• logo, all the courses, and our phone number email and address.
Nice to have
• pricing, and maybe saying something like, Additional courses insure that you are providing as many services as possible to your clients and in return you gain customer loyalty. (Reword)
Should not have
• cheesy.

```html
<!DOCTYPE html>
<html lang="en">
<head>
<meta charset="utf-8">
<title>VGW Academy – Beauty Courses</title>
<link rel="stylesheet" href="https://fonts.googleapis.com/css2?family=Cormorant+Garamond:wght@500&family=Lato:wght@400;700;900&display=swap">
<style>
  :root {
    --frame-grey: #aaaaaa;
    --panel-black: #141414;
    --heading-pink: #f26d72;
    --pill-red: #d9534f;
    --title-grey: #a3a3a3;
    --text-white: #ffffff;
    --logo-black: #000000;
  }
  * { margin: 0; padding: 0; box-sizing: border-box; }
  html, body { width: 846px; height: 1200px; overflow: hidden; }
  body {
    position: relative;
    background: var(--frame-grey);
    font-family: "Lato", Arial, sans-serif;
    color: var(--text-white);
  }
  .flyer-panel {
    position: absolute; left: 10px; top: 10px; width: 826px; height: 1046px;
    background: var(--panel-black); overflow: hidden;
  }
  .model-photo {
    position: absolute; left: 446px; top: 420px; width: 380px; height: 626px;
    background:
      radial-gradient(ellipse 55% 45% at 62% 62%, rgba(150,110,95,0.55), rgba(60,45,40,0.35) 55%, transparent 80%),
      radial-gradient(ellipse 60% 30% at 70% 20%, rgba(20,20,22,0.9), transparent 70%),
      radial-gradient(ellipse 50% 40% at 10% 40%, rgba(35,55,35,0.5), transparent 75%);
  }
  .abs { position: absolute; }
  .academy-title {
    left: 40px; top: 52px;
    font-family: "Cormorant Garamond", "Times New Roman", serif;
    font-weight: 500; font-size: 58px; letter-spacing: 1px;
    color: var(--title-grey); line-height: 1;
  }
  .audience-line {
    right: 50px; top: 54px; text-align: right;
    font-weight: 900; font-size: 14.5px; line-height: 18px; letter-spacing: 0.3px;
  }
  .course-name {
    left: 40px; font-weight: 400; font-size: 31px; line-height: 38px;
    color: var(--heading-pink);
  }
  .course-detail {
    left: 40px; width: 420px; font-weight: 700; font-size: 17.5px; line-height: 22px;
  }
  .price-pill {
    width: 68px; height: 34px; border-radius: 17px;
    background: var(--pill-red);
    font-weight: 700; font-size: 20px; line-height: 34px; text-align: center;
  }
  .bundle-block { right: 48px; text-align: right; font-size: 20px; line-height: 23px; font-weight: 700; }
  .bundle-heading { right: 48px; font-size: 20px; font-weight: 700; color: var(--heading-pink); }
  .bundle-name { color: var(--heading-pink); font-weight: 400; }
  .inquiry-label { left: 40px; font-size: 19px; font-weight: 700; }
  .inquiry-phone { left: 40px; top: 916px; font-size: 37px; font-weight: 700; color: var(--heading-pink); letter-spacing: 0.5px; }
  .brand-mark {
    position: absolute; left: 0; top: 1056px; width: 846px; height: 144px;
    display: flex; align-items: center; justify-content: center; gap: 16px;
  }
  .brand-dot { width: 30px; height: 30px; border-radius: 50%; background: var(--logo-black); }
  .brand-name { font-weight: 900; font-size: 40px; letter-spacing: 3px; color: var(--logo-black); }
</style>
</head>
<body>
  <section class="flyer-panel">
    <div class="model-photo" role="img" aria-label="Photo of a woman in a black hat with long eyelash extensions, eyes lowered"></div>

    <h1 class="abs academy-title">VGW ACADEMY</h1>
    <p class="abs audience-line">BEAUTY COURSES FOR<br>COSMOTOLOGY STUDENTS &amp;<br>INDUSTRY PROFESSIONALS</p>

    <h2 class="abs course-name" style="top:160px">Eyelash Enhancement<br>Classic Extension</h2>
    <div class="abs price-pill" style="left:369px;top:192px">$350</div>
    <p class="abs course-detail" style="top:241px">Day Course. Comes with a kit that should last<br>the students through 30 clients.</p>

    <h2 class="abs course-name" style="top:322px">Eyelash Enhancement<br>Russian Volume</h2>
    <div class="abs price-pill" style="left:369px;top:348px">$450</div>
    <p class="abs course-detail" style="top:406px">Day Course. Comes with a kit that should last<br>the students through 30 clients.</p>

    <h2 class="abs course-name" style="top:484px">Threading Hair<br>Removal</h2>
    <div class="abs price-pill" style="left:369px;top:513px">$100</div>
    <p class="abs course-detail" style="top:576px">1/2 Day course. Comes with a kit that should<br>last students through 60 clients. Students will<br>need 3 Models for Eyebrow Threading</p>

    <h2 class="abs course-name" style="top:682px">Spray Tanning</h2>
    <div class="abs price-pill" style="left:369px;top:682px">$100</div>
    <p class="abs course-detail" style="top:730px">1/2 Day course. Students will have an<br>"add-on" kit that will get them a Spray tan<br>&nbsp;Machine with 3 basic colors to last them<br>&nbsp;through 300 clients.</p>

    <h3 class="abs bundle-heading" style="top:170px">BUNDLE DEALS:</h3>
    <p class="abs bundle-block" style="top:220px">
      <span class="bundle-name">Lash Pro Bundle</span><br>
      Learn Eyelash<br>Enhancement both<br>Classic and Volume<br>Extensions. 4 day course<br>with 2 kits for each<br>technique.
    </p>
    <div class="abs price-pill" style="left:710px;top:416px">$850</div>
    <p class="abs bundle-block" style="top:510px">
      <span class="bundle-name">Velvet Pro Bundle</span><br>All courses combined.
    </p>
    <div class="abs price-pill" style="left:710px;top:576px">$650</div>

    <p class="abs inquiry-label" style="top:884px">for inquiries call</p>
    <p class="abs inquiry-phone">949-387-6120</p>
    <p class="abs inquiry-label" style="top:974px">or email us on</p>
    <p class="abs inquiry-label" style="top:1000px">kelseyportland@velvetgloworks.com</p>
  </section>

  <footer class="brand-mark">
    <span class="brand-dot"></span>
    <span class="brand-name">VELVET GLOW WORKS</span>
  </footer>
</body>
</html>
```